Tallow Farm Brochure

To design a small brochure that tells people about our U-Pick cherry farm, where we are, when we are open and what our contact details are.

We have existing logo's which should be used. I have uploaded a file with these details.

Details about us are all located on:-
www.friendlink.example/tallowfarm
https://circlepage.example/u/0/b/704916382057419263851/704916382057419263851/about/p/pub

Farm

```html
<!DOCTYPE html>
<html lang="en">
<head>
<meta charset="utf-8">
<title>Tallow Farm Brochure</title>
<link rel="stylesheet" href="https://fonts.googleapis.com/css2?family=Arimo:ital,wght@0,700;1,700&family=Lato:wght@400;700&display=swap">
<style>
  :root {
    --page: #e4e6e5;
    --teal-deep: #0b8f72;
    --teal: #17a887;
    --teal-light: #22b897;
    --lime: #b9dc3c;
    --lime-dark: #8fc232;
    --quote: #d9ea4c;
    --ink-green: #0f7a5e;
    --white: #ffffff;
    --pill-top: #ffffff;
    --pill-bottom: #d5d8d7;
  }
  * { margin: 0; padding: 0; box-sizing: border-box; }
  html, body { width: 1200px; height: 900px; overflow: hidden; }
  body {
    background: var(--page);
    font-family: "Lato", Arial, sans-serif;
    color: var(--white);
    position: relative;
  }
  .brochure {
    position: absolute;
    left: 85px; top: 80px;
    width: 1020px; height: 728px;
    background: linear-gradient(180deg, var(--teal-light) 0%, var(--teal) 45%, var(--teal-deep) 100%);
    overflow: hidden;
    box-shadow: 0 6px 18px rgba(0,0,0,0.25);
  }
  .fold { position: absolute; top: 0; bottom: 0; width: 40px; }
  .fold-left { left: 327px; background: linear-gradient(90deg, rgba(0,0,0,0) 0%, rgba(0,0,0,0.12) 50%, rgba(0,0,0,0) 100%); }
  .fold-right { left: 663px; background: linear-gradient(90deg, rgba(0,0,0,0) 0%, rgba(0,0,0,0.12) 50%, rgba(0,0,0,0) 100%); }
  .sweep { position: absolute; left: 0; top: 0; }
  .bottom-strip {
    position: absolute; left: 0; right: 0; bottom: 0; height: 13px;
    background: linear-gradient(90deg, var(--lime-dark), var(--lime));
  }
  .pill {
    position: absolute;
    background: linear-gradient(180deg, var(--pill-top), var(--pill-bottom));
    color: var(--ink-green);
    box-shadow: 0 3px 6px rgba(0,0,0,0.25);
    display: flex; align-items: center;
  }
  .about-title {
    left: 0; top: 234px; width: 243px; height: 42px;
    border-radius: 0 21px 21px 0;
    padding-left: 24px;
    font-family: "Arimo", Arial, sans-serif;
    font-weight: 700; font-size: 34px;
  }
  .about-text {
    position: absolute; left: 26px; top: 309px; width: 290px;
    font-size: 14px; line-height: 19.5px;
  }
  .about-text p + p { margin-top: 6px; }
  .quote {
    position: absolute; left: 25px; top: 527px; width: 308px;
    font-family: "Arimo", Arial, sans-serif;
    font-style: italic; font-weight: 700;
    font-size: 15px; line-height: 19.5px;
    color: var(--quote);
    text-align: justify;
  }
  .quote-author {
    position: absolute; left: 25px; top: 602px; width: 302px;
    text-align: right; font-weight: 700; font-size: 16px;
  }
  .left-url {
    left: 0; top: 652px; width: 306px; height: 42px;
    border-radius: 0 21px 21px 0;
    padding-left: 28px;
    font-weight: 700; font-size: 19px;
  }
  .hours {
    position: absolute; left: 431px; top: 295px; width: 160px; height: 160px;
    border-radius: 50%;
    background: linear-gradient(180deg, #ffffff, #d9dcdb);
    border: 6px solid var(--lime);
    box-shadow: 0 4px 10px rgba(0,0,0,0.3);
    display: flex; flex-direction: column; align-items: center; justify-content: center;
    color: var(--ink-green);
  }
  .hours-days { font-family: "Arimo", Arial, sans-serif; font-weight: 700; font-size: 30px; line-height: 34px; }
  .hours-time { font-size: 19px; line-height: 24px; }
  .map {
    position: absolute; left: 400px; top: 476px; width: 223px; height: 88px;
    background: linear-gradient(135deg, #eceee9, #dfe3dc);
    border: 2px solid #f4f4f4;
  }
  .contact {
    position: absolute; left: 347px; width: 336px;
    list-style: none; text-align: center; font-size: 16px;
  }
  .contact li { position: relative; }
  .contact-address { top: 588px; line-height: 20px; }
  .contact-phone { top: 638px; }
  .contact-web { top: 665px; }
  .icon {
    display: inline-block; width: 12px; height: 12px; border-radius: 50%;
    background: var(--lime); margin-right: 8px; vertical-align: 0;
    position: relative;
  }
  .icon svg { position: absolute; left: 2px; top: 2px; }
  .brand-name {
    position: absolute; left: 683px; width: 337px; top: 518px;
    text-align: center; font-weight: 400; color: var(--white);
    display: flex; flex-direction: column; align-items: center;
  }
  .brand-mark { width: 14px; height: 14px; border-radius: 50%; background: var(--white); margin-bottom: 6px; }
  .brand-line-1 { font-size: 60px; line-height: 62px; }
  .brand-line-2 { font-size: 40px; line-height: 42px; }
  .right-url {
    left: 725px; top: 661px; width: 247px; height: 32px;
    border-radius: 16px; justify-content: center;
    font-weight: 700; font-size: 16px;
  }
</style>
</head>
<body>
  <main class="brochure">
    <div class="fold fold-left"></div>
    <div class="fold fold-right"></div>

    <svg class="sweep" width="1020" height="728" viewBox="0 0 1020 728">
      <defs>
        <linearGradient id="limeBand" x1="0" y1="0" x2="1" y2="0">
          <stop offset="0" stop-color="#8fc232"/>
          <stop offset="1" stop-color="#c7e34a"/>
        </linearGradient>
        <linearGradient id="photoFill" x1="0" y1="0" x2="1" y2="1">
          <stop offset="0" stop-color="#8db455"/>
          <stop offset="1" stop-color="#5f8a34"/>
        </linearGradient>
      </defs>
      <path d="M140 0 H1020 V448 C760 432 540 372 390 282 C280 212 200 122 140 0 Z" fill="url(#limeBand)"/>
      <path d="M168 0 H1020 V418 C770 408 560 350 410 264 C305 202 225 115 168 0 Z" fill="#f2f4ee"/>
      <path d="M185 0 H1020 V400 C770 392 570 336 425 252 C325 194 240 110 185 0 Z" fill="url(#photoFill)" role="img" aria-label="Photo of the cherry orchard"/>
      <path d="M200 0 C255 110 340 190 440 246 C585 326 780 372 1020 380" fill="none" stroke="#ffffff" stroke-width="2.5"/>
    </svg>

    <section class="about">
      <h1 class="pill about-title">About us</h1>
      <div class="about-text">
        <p>Tallow Farm is in the beautiful Brindle Valley, an ideallocation for growing sweet juicy cherries. Visit us for Pick Your Own or Pre-Picked Cherries.</p>
        <p>When you first arrive at our farm we can show you how to pick cherries and where the best cherries are on that day. Farmer Ned can also show you around the farm and explain how the cherries are grown and the organic principles we employ in managing our trees.</p>
      </div>
      <p class="quote">It's the magnificent views and our happy trees. That's what makes our cherries juicier and sweeter.</p>
      <p class="quote-author">-Farmer Ned</p>
      <p class="pill left-url">www.tallowfarm.example</p>
    </section>

    <section class="visit">
      <div class="hours">
        <span class="hours-days">Fri - Sun</span>
        <span class="hours-time">10:00 - 17:00</span>
      </div>
      <div class="map" role="img" aria-label="Street map showing the farm location"></div>
      <ul class="contact contact-address"><li><span class="icon"><svg width="8" height="8" viewBox="0 0 8 8"><path d="M4 0.5 L7.5 4 H6.5 V7.5 H1.5 V4 H0.5 Z" fill="#0f7a5e"/></svg></span>48 Kestrel-Tallow Road, Tallow,<br>Victoria 3199</li></ul>
      <ul class="contact contact-phone"><li><span class="icon"><svg width="8" height="8" viewBox="0 0 8 8"><path d="M1.5 0.8 L3 2.6 L2.3 3.4 C2.8 4.5 3.5 5.2 4.6 5.7 L5.4 5 L7.2 6.5 L6.4 7.4 C3.5 7.2 0.8 4.5 0.6 1.6 Z" fill="#0f7a5e"/></svg></span>1300 48 20 71</li></ul>
      <ul class="contact contact-web"><li><span class="icon"><svg width="8" height="8" viewBox="0 0 8 8"><circle cx="4" cy="4" r="3.2" fill="none" stroke="#0f7a5e" stroke-width="1"/></svg></span>www.tallowfarm.example</li></ul>
    </section>

    <section class="cover">
      <div class="brand-name">
        <span class="brand-mark"></span>
        <span class="brand-line-1">Tallow</span>
        <span class="brand-line-2">Farm</span>
      </div>
      <p class="pill right-url">www.tallowfarm.example</p>
    </section>

    <div class="bottom-strip"></div>
  </main>
</body>
</html>
```